Deisgn A Manual Cover for an Australian Health Training Company

We are looking for an A4 Front of Manual Cover Design for a comprehensive administrative training manual to be launched soon in Australia.

The title of the book is :

"Drafting, Shaping and Delivering Office Paperwork"

for the Australian Medical Office (smaller font)

Written and compiled by Mel Trosk

Target Market(s)

25-45 year old medical administrative students (usually female)

Industry/Entity Type

It Company

Font styles to use
Serif

Colors
3176b5
f68d4c
33b8a4
fffbf0

Requirements
Must have
• University like perhaps
• Human element (picture/s of people)
• About the concept of designing and producing documents in a health setting (this can be entirely conceptual).
• Conceptual design would be considered
• Appealing

```html
<!DOCTYPE html>
<html lang="en">
<head>
<meta charset="UTF-8">
<title>Drafting, Shaping and Delivering Office Paperwork — Manual Cover</title>
<link href="https://fonts.googleapis.com/css2?family=Oswald:wght@400;500;700&family=Josefin+Sans:wght@400;600&display=swap" rel="stylesheet">
<style>
  :root {
    --blue: #3176b5;
    --band-blue: #2f66a3;
    --orange: #f68d4c;
    --teal: #33b8a4;
    --cream: #fffbf0;
    --paper: #ffffff;
    --ink-grey: #6f7479;
    --rule-grey: #9a9fa4;
    --navy: #1f3552;
    --backdrop: #8ea8b4;
    --skin-light: #f6d7b8;
    --skin: #eab88f;
    --heart-red: #e8474a;
  }
  * { box-sizing: border-box; margin: 0; padding: 0; }
  html, body {
    width: 1200px;
    height: 784px;
    overflow: hidden;
  }
  body {
    background: var(--backdrop);
    display: flex;
    align-items: center;
    justify-content: center;
  }
  .cover {
    position: relative;
    width: 510px;
    height: 722px;
    background: var(--paper);
    display: flex;
    flex-direction: column;
    align-items: center;
    font-family: "Oswald", sans-serif;
    box-shadow: 0 6px 18px rgba(0, 0, 0, 0.18);
  }
  .institute {
    margin-top: 22px;
    display: flex;
    align-items: center;
    gap: 6px;
  }
  .institute-mark {
    width: 12px;
    height: 12px;
    background: var(--navy);
  }
  .institute-name {
    font-weight: 500;
    font-size: 10px;
    letter-spacing: 0.08em;
    text-transform: uppercase;
    color: var(--navy);
  }
  .title {
    margin-top: 24px;
    width: 370px;
    text-transform: uppercase;
    font-weight: 700;
    line-height: 0.95;
    text-align: center;
  }
  .title-line { display: block; }
  .title-drafting { color: var(--blue); font-size: 76px; }
  .title-shaping { color: var(--orange); font-size: 72px; }
  .title-and {
    display: flex;
    align-items: center;
    gap: 8px;
    margin: 2px 0 4px;
    font-size: 9px;
    font-weight: 500;
    color: var(--ink-grey);
    letter-spacing: 0.1em;
  }
  .title-and::before, .title-and::after {
    content: "";
    flex: 1;
    height: 2px;
    background: var(--rule-grey);
  }
  .title-delivering { color: var(--teal); font-size: 64px; }
  .title-paperwork { color: var(--teal); font-size: 34px; margin-top: 4px; }
  .subtitle {
    display: flex;
    align-items: center;
    gap: 8px;
    width: 320px;
    margin-top: 6px;
    font-size: 10px;
    font-weight: 500;
    letter-spacing: 0.04em;
    text-transform: uppercase;
    color: var(--ink-grey);
  }
  .subtitle::before, .subtitle::after {
    content: "";
    flex: 1;
    height: 1px;
    background: var(--rule-grey);
  }
  .artwork {
    margin-top: auto;
    width: 400px;
    height: 230px;
    border-radius: 110px 110px 0 0;
    background: linear-gradient(180deg, var(--heart-red) 0%, #ef8f78 30%, var(--skin) 65%, var(--skin-light) 100%);
  }
  .author-band {
    width: 100%;
    height: 92px;
    background: var(--band-blue);
    display: flex;
    flex-direction: column;
    align-items: center;
    justify-content: center;
    color: var(--paper);
    font-family: "Josefin Sans", sans-serif;
  }
  .author-credit {
    display: flex;
    align-items: center;
    gap: 8px;
    font-size: 11px;
    font-weight: 600;
    letter-spacing: 0.12em;
    text-transform: uppercase;
  }
  .author-credit::before, .author-credit::after {
    content: "";
    width: 40px;
    height: 1px;
    background: var(--paper);
  }
  .author-name {
    margin-top: 6px;
    font-size: 40px;
    font-weight: 400;
    letter-spacing: 0.1em;
    text-transform: uppercase;
  }
</style>
</head>
<body>
  <main class="cover">
    <header class="institute">
      <span class="institute-mark"></span>
      <span class="institute-name">Harbourline Institute of Training</span>
    </header>

    <h1 class="title">
      <span class="title-line title-drafting">Drafting,</span>
      <span class="title-line title-shaping">Shaping</span>
      <span class="title-line title-and">and</span>
      <span class="title-line title-delivering">Delivering</span>
      <span class="title-line title-paperwork">Office Paperwork</span>
    </h1>
    <p class="subtitle">For the Australian Medical Office</p>

    <div class="artwork" role="img" aria-label="Illustration of raised hands holding a red heart in the centre, a medical document with a red cross on the left and a clipboard on the right"></div>

    <footer class="author-band">
      <p class="author-credit">Written and compiled by</p>
      <p class="author-name">Mel Trosk</p>
    </footer>
  </main>
</body>
</html>
```